Product Page Images & A+ Content Design for TCG Storage Products

Create a new, cohesive set of Zentoro product images (all secondary gallery images) and A+ content modules for Ember Hollow Protective Card Sleeves. The goal is to clearly communicate protection, fit, clarity, and archival safety while looking more premium and distinctive than competing sleeve brands.

Primary benefits to communicate:
- Shield your cards from wear – blocks dust and resists surface scratches.
- The perfect fit for your collection – designed to fit all standard trading cards.
- Ultra‑clear smooth finish.
- Archival‑safe high‑quality materials – acid‑free, no PVC, non‑toxic, long‑term storage.

Tone: Premium but approachable, aimed at TCG players and collectors (Glimmerbeasts, SRQ, Zan‑Ko‑Ra!, sports cards, etc.). Colour/theme be in keeping with the packaging design. Dark, with a pop of orange. Perhaps subtle textures or patterns, with a mythic/fantasy feel.

Existing product content is attached for reference.

Target Market(s)

Trading card game players and collectors (Glimmerbeasts‑style TCGs, SRQ‑style games, Zan‑Ko‑Ra!‑style games, sports cards). Age: Mainly 14–40, skewed to hobbyist young adults. They care about condition and long‑term value of their cards, enjoy customising and protecting decks, responsive to “premium but good value” messaging.

Industry/Entity Type

Trading card accessories / tabletop gaming accessories. Protective sleeves and storage for trading card games and sports cards.

Font styles to use
Sans Serif

Requirements
Must have
• Clear communication of the four key benefits listed in the Project Description. Consistent use of Ember Hollow logo and brand colours. Text that is readable on mobile thumbnails. Clean, uncluttered layouts that look professional next to leading competitors.
Nice to have
• Subtle fantasy / “mythic” visual touches that support the brand name (background textures, icons, gentle glow effects). Simple line‑art icons for key benefits (dust, scratch, fit, clarity, archival safe). Visual references to different card types (TCG, sports, etc.) using generic, non‑IP artwork. Light environmental storytelling (desk, playmat, storage box, binder). Lifestyle shots showing people playing or organising their collections.
Should not have
• Any copyrighted or licensed character artwork or logos. Over‑busy backgrounds or textures that distract from the product. Very long text blocks or small copy that is hard to read on mobile. Edgy, aggressive, or dark imagery that clashes with a family‑friendly hobby product. Inconsistent typography or colour schemes across images.

```html
<!DOCTYPE html>
<html lang="en">
<head>
<meta charset="utf-8">
<title>Ember Hollow – Protective Card Sleeves Gallery Set</title>
<link rel="stylesheet" href="https://fonts.googleapis.com/css2?family=Poppins:wght@400;500;600&family=Roboto+Slab:wght@800&display=swap">
<style>
:root{
  --page:#ebebeb;
  --ink:#0b0b0b;
  --ink-soft:#1c1c1c;
  --paper:#ffffff;
  --paper-shade:#eeeeee;
  --ember:#ff4a0a;
  --gold:#c7b287;
  --sleeve:#d9dcdf;
  --card-dark:#1d2a3a;
  --card-mid:#3f6c94;
  --card-glow:#8fb7d6;
}
*{margin:0;padding:0;box-sizing:border-box}
html,body{width:1200px;height:2821px;overflow:hidden;background:var(--page)}
body{position:relative;font-family:"Poppins",sans-serif;color:var(--ink)}

.banner{position:absolute;left:117px;width:965px;height:298px;overflow:hidden;box-shadow:0 10px 24px rgba(0,0,0,.18)}
.banner--dark{background:linear-gradient(100deg,#050505 0%,#1a1a1a 45%,#060606 100%)}
.banner--light{background:radial-gradient(ellipse at 45% 40%,var(--paper) 0%,var(--paper-shade) 100%)}
.shapes{position:absolute;inset:0;width:100%;height:100%}

.brand{position:absolute;font-family:"Poppins",sans-serif;font-weight:600;color:var(--gold);font-size:24px;line-height:1;letter-spacing:1px;text-transform:uppercase}
.brand span{display:block;margin-top:4px}

.headline{position:absolute;z-index:2;font-family:"Roboto Slab",serif;font-weight:800;text-transform:uppercase;line-height:1;white-space:nowrap;letter-spacing:0}
.accent{color:var(--ember)}
.headline--light{color:var(--paper)}
.subline{position:absolute;z-index:2;font-family:"Poppins",sans-serif;font-weight:400;white-space:nowrap;line-height:1.1}

.benefit{position:absolute;display:flex;align-items:center;gap:11px;white-space:nowrap;font-size:22px}
.benefit svg{flex:none}
.benefit--light{color:var(--paper)}
.benefit--small{font-size:16px;line-height:1.15;align-items:center}

.card{position:absolute;border:5px solid var(--sleeve);border-radius:4px;
  background:radial-gradient(circle at 50% 35%,var(--card-glow) 0%,var(--card-mid) 35%,var(--card-dark) 75%);
  box-shadow:0 4px 10px rgba(0,0,0,.35)}
.card::after{content:"";position:absolute;left:6%;right:6%;bottom:6%;height:26%;background:#e9e6df;border-radius:2px}
.card-frame{position:absolute;border:2px solid var(--ember);border-radius:4px;background:rgba(255,255,255,.6)}
</style>
</head>
<body>

<!-- 1: Hero -->
<section class="banner banner--dark" style="top:159px">
  <div class="brand" style="left:40px;top:70px">Ember<span>Hollow</span></div>
  <h1 class="headline headline--light" style="left:266px;top:58px;font-size:39px">Protective</h1>
  <p class="headline accent" style="left:266px;top:96px;font-size:39px">Card Sleeves</p>

  <div class="benefit benefit--light" style="left:32px;top:228px">
    <svg width="44" height="44" viewBox="0 0 44 44"><circle cx="22" cy="22" r="19" fill="none" stroke="var(--ember)" stroke-width="3"/><circle cx="22" cy="22" r="13" fill="var(--paper)"/><path d="M22 14l6 2.5v5c0 4-2.6 6.6-6 8-3.4-1.4-6-4-6-8v-5z" fill="var(--ink)"/></svg>Protection</div>
  <div class="benefit benefit--light" style="left:210px;top:228px">
    <svg width="44" height="44" viewBox="0 0 44 44"><circle cx="22" cy="22" r="19" fill="none" stroke="var(--ember)" stroke-width="3"/><circle cx="22" cy="22" r="13" fill="var(--paper)"/><path d="M15 15l5 5M29 15l-5 5M15 29l5-5M29 29l-5-5" stroke="var(--ink)" stroke-width="3"/></svg>Fit</div>
  <div class="benefit benefit--light" style="left:303px;top:228px">
    <svg width="44" height="44" viewBox="0 0 44 44"><circle cx="22" cy="22" r="19" fill="none" stroke="var(--ember)" stroke-width="3"/><circle cx="22" cy="22" r="13" fill="var(--paper)"/><path d="M13 22q9-8 18 0q-9 8-18 0z" fill="var(--ink)"/><circle cx="22" cy="22" r="3" fill="var(--paper)"/></svg>Clarity</div>
  <div class="benefit benefit--light" style="left:441px;top:228px">
    <svg width="44" height="44" viewBox="0 0 44 44"><circle cx="22" cy="22" r="19" fill="none" stroke="var(--ember)" stroke-width="3"/><circle cx="22" cy="22" r="13" fill="var(--paper)"/><path d="M16 22l4 4 8-9" fill="none" stroke="var(--ink)" stroke-width="3"/></svg>Safety</div>

  <div class="card" role="img" aria-label="Sleeved trading card with generic fantasy creature artwork" style="left:590px;top:69px;width:104px;height:172px"></div>
  <div class="card" role="img" aria-label="Sleeved trading card with generic fantasy creature artwork" style="left:826px;top:69px;width:104px;height:172px"></div>
  <div class="card" role="img" aria-label="Sleeved trading card with generic fantasy creature artwork, front view" style="left:692px;top:33px;width:136px;height:208px"></div>

  <svg class="shapes" viewBox="0 0 965 298" aria-hidden="true">
    <rect x="0" y="280" width="965" height="18" fill="var(--paper)"/>
    <g fill="var(--ember)">
      <polygon points="47,280 92,280 80,298 35,298"/>
      <polygon points="142,280 192,280 180,298 130,298"/>
      <polygon points="452,280 502,280 490,298 440,298"/>
      <polygon points="547,280 597,280 585,298 535,298"/>
      <polygon points="642,280 692,280 680,298 630,298"/>
    </g>
    <g fill="var(--ink)">
      <polygon points="100,280 125,280 113,298 88,298"/>
      <polygon points="505,280 540,280 528,298 493,298"/>
      <polygon points="598,280 635,280 623,298 586,298"/>
    </g>
  </svg>
</section>

<!-- 2: Brand showcase -->
<section class="banner banner--dark" style="top:600px">
  <div class="card" role="img" aria-label="Sleeved trading card, tilted" style="left:50px;top:75px;width:112px;height:190px;transform:rotate(-9deg)"></div>
  <div class="card" role="img" aria-label="Sleeved trading card, tilted" style="left:147px;top:30px;width:140px;height:225px;transform:rotate(8deg)"></div>
  <div class="brand" style="left:372px;top:124px;font-size:32px;width:220px;text-align:center">Ember<span>Hollow</span></div>
  <div class="card" role="img" aria-label="Sleeved trading card, mirrored view" style="left:678px;top:30px;width:140px;height:225px;transform:rotate(-8deg)"></div>
  <div class="card" role="img" aria-label="Sleeved trading card, tilted" style="left:803px;top:75px;width:112px;height:190px;transform:rotate(9deg)"></div>
</section>

<!-- 3: Shield from wear -->
<section class="banner banner--light" style="top:1040px">
  <svg class="shapes" viewBox="0 0 965 298" aria-hidden="true">
    <rect x="0" y="0" width="965" height="30" fill="var(--ink)"/>
    <polygon points="0,0 460,0 376,137 0,137" fill="var(--ink)"/>
    <polygon points="530,38 588,38 576,55 518,55" fill="var(--ember)"/>
    <polygon points="588,38 634,38 622,55 576,55" fill="var(--ink)"/>
    <polygon points="634,38 692,38 680,55 622,55" fill="var(--ember)"/>
    <polygon points="692,38 738,38 726,55 680,55" fill="var(--ink)"/>
    <polygon points="738,38 796,38 784,55 726,55" fill="var(--ember)"/>
    <polygon points="796,38 965,38 965,55 784,55" fill="var(--ink)"/>
  </svg>
  <div class="brand" style="left:40px;top:56px">Ember<span>Hollow</span></div>
  <h2 class="headline" style="left:32px;top:155px;font-size:37px"><span class="accent">Shield your cards</span> from wear</h2>
  <p class="subline" style="left:32px;top:193px;font-size:29px">Blocks dust and resists surface scratches</p>
  <div class="benefit" style="left:32px;top:232px">
    <svg width="44" height="44" viewBox="0 0 44 44"><circle cx="22" cy="22" r="22" fill="var(--ink)"/><path d="M14 22h12M14 17h8M14 27h8" stroke="var(--paper)" stroke-width="2.5"/><path d="M26 15l6 7-6 7z" fill="var(--paper)"/></svg>Dust Protection</div>
  <div class="benefit" style="left:290px;top:232px">
    <svg width="44" height="44" viewBox="0 0 44 44"><circle cx="22" cy="22" r="22" fill="var(--ember)"/><path d="M14 28l14-14M18 31l13-13M13 23l10-10" stroke="var(--paper)" stroke-width="2.5" stroke-linecap="round"/></svg>Scratch Resistant</div>
  <div class="card-frame" style="left:800px;top:77px;width:133px;height:190px"></div>
  <div class="card" role="img" aria-label="Sleeved trading card with generic fantasy creature artwork" style="left:812px;top:88px;width:108px;height:166px"></div>
</section>

<!-- 4: Perfect fit -->
<section class="banner banner--light" style="top:1481px">
  <svg class="shapes" viewBox="0 0 965 298" aria-hidden="true">
    <rect x="0" y="0" width="965" height="23" fill="var(--ink)"/>
    <polygon points="0,0 430,0 335,137 0,137" fill="var(--ink)"/>
    <polygon points="448,0 506,0 494,23 436,23" fill="var(--ember)"/>
    <polygon points="512,0 520,0 508,23 500,23" fill="var(--paper)"/>
    <polygon points="568,0 626,0 614,23 556,23" fill="var(--ember)"/>
    <polygon points="632,0 640,0 628,23 620,23" fill="var(--paper)"/>
    <polygon points="683,0 741,0 729,23 671,23" fill="var(--ember)"/>
    <polygon points="0,274 530,274 515,298 0,298" fill="var(--ink)"/>
    <polygon points="255,274 328,274 343,298 270,298" fill="var(--ember)"/>
    <polygon points="427,274 500,274 515,298 442,298" fill="var(--ember)"/>
  </svg>
  <div class="brand" style="left:40px;top:56px">Ember<span>Hollow</span></div>
  <div class="card-frame" style="left:735px;top:37px;width:190px;height:228px;transform:rotate(-3deg)"></div>
  <div class="card" role="img" aria-label="Sleeved trading card sitting snugly in its sleeve" style="left:752px;top:50px;width:155px;height:200px;transform:rotate(2deg)"></div>
  <h2 class="headline" style="left:34px;top:168px;font-size:28px"><span class="accent">The perfect</span> fit for your collection</h2>
  <p class="subline" style="left:32px;top:205px;font-size:29px">Designed to fit all standard trading cards</p>
</section>

<!-- 5: Ultra-clear -->
<section class="banner" style="top:1923px;background:var(--ink)">
  <svg class="shapes" viewBox="0 0 965 298" aria-hidden="true">
    <defs><radialGradient id="paperGlow" cx="35%" cy="40%" r="70%"><stop offset="0" stop-color="#ffffff"/><stop offset="1" stop-color="#eeeeee"/></radialGradient></defs>
    <polygon points="296,0 797,0 590,281 0,281 0,137 200,137" fill="url(#paperGlow)"/>
    <rect x="0" y="281" width="965" height="17" fill="var(--paper)"/>
    <g fill="var(--ember)">
      <polygon points="12,281 54,281 42,298 0,298"/>
      <polygon points="102,281 150,281 138,298 90,298"/>
      <polygon points="435,281 480,281 468,298 423,298"/>
      <polygon points="528,281 576,281 564,298 516,298"/>
      <polygon points="628,281 678,281 666,298 616,298"/>
    </g>
    <g fill="var(--ink)">
      <polygon points="60,281 94,281 82,298 48,298"/>
      <polygon points="158,281 185,281 173,298 146,298"/>
      <polygon points="485,281 520,281 508,298 473,298"/>
      <polygon points="582,281 620,281 608,298 570,298"/>
    </g>
  </svg>
  <div class="brand" style="left:36px;top:56px">Ember<span>Hollow</span></div>
  <div class="card" role="img" aria-label="Sleeved trading card with generic fantasy creature artwork" style="left:594px;top:94px;width:100px;height:173px"></div>
  <div class="card" role="img" aria-label="Sleeved trading card with generic fantasy creature artwork" style="left:833px;top:94px;width:100px;height:173px"></div>
  <div class="card" role="img" aria-label="Sleeved trading card with generic fantasy creature artwork, front view" style="left:690px;top:34px;width:146px;height:230px"></div>
  <h2 class="headline" style="left:275px;top:44px;font-size:36px">Ultra-clear</h2>
  <p class="headline accent" style="left:275px;top:80px;font-size:36px">Smooth finish</p>
  <div class="benefit benefit--small" style="left:33px;top:170px;gap:18px">
    <svg width="48" height="48" viewBox="0 0 48 48"><circle cx="24" cy="24" r="24" fill="var(--ink)"/><path d="M13 24q11-10 22 0q-11 10-22 0z" fill="none" stroke="var(--paper)" stroke-width="2.5"/><circle cx="24" cy="24" r="4" fill="var(--paper)"/></svg>
    <span>Enjoy crystal clear<br>visibility for vibrant<br>artwork &amp; sharp details</span></div>
  <div class="benefit benefit--small" style="left:292px;top:168px;gap:18px">
    <svg width="48" height="48" viewBox="0 0 48 48"><circle cx="24" cy="24" r="24" fill="var(--ember)"/><path d="M17 33l12-16M23 34l8-11" stroke="var(--paper)" stroke-width="3" stroke-linecap="round"/></svg>
    <span>Silky smooth<br>feel that makes<br>shuffling easy</span></div>
</section>

<!-- 6: Archival-safe -->
<section class="banner banner--light" style="top:2364px">
  <svg class="shapes" viewBox="0 0 965 298" aria-hidden="true">
    <rect x="0" y="0" width="965" height="30" fill="var(--ink)"/>
    <polygon points="0,0 460,0 376,137 0,137" fill="var(--ink)"/>
    <polygon points="530,38 588,38 576,55 518,55" fill="var(--ember)"/>
    <polygon points="588,38 634,38 622,55 576,55" fill="var(--ink)"/>
    <polygon points="634,38 692,38 680,55 622,55" fill="var(--ember)"/>
    <polygon points="692,38 738,38 726,55 680,55" fill="var(--ink)"/>
    <polygon points="738,38 796,38 784,55 726,55" fill="var(--ember)"/>
    <polygon points="796,38 965,38 965,55 784,55" fill="var(--ink)"/>
    <polygon points="0,202 363,202 452,298 0,298" fill="var(--ember)"/>
  </svg>
  <div class="brand" style="left:40px;top:56px">Ember<span>Hollow</span></div>
  <div class="card-frame" style="left:798px;top:71px;width:134px;height:193px"></div>
  <div class="card" role="img" aria-label="Sleeved trading card with generic fantasy creature artwork" style="left:811px;top:83px;width:108px;height:168px"></div>
  <h2 class="headline" style="left:34px;top:156px;font-size:30px"><span class="accent">Archival-safe</span> high quality materials</h2>
  <div class="benefit benefit--light" style="left:34px;top:226px">
    <svg width="52" height="52" viewBox="0 0 52 52"><circle cx="26" cy="26" r="24" fill="var(--paper)"/><circle cx="26" cy="26" r="20" fill="var(--ink)"/><path d="M26 14q8 10 8 16a8 8 0 0 1-16 0q0-6 8-16z" fill="var(--paper)"/></svg>Acid-free</div>
  <div class="benefit benefit--light" style="left:214px;top:226px">
    <svg width="52" height="52" viewBox="0 0 52 52"><circle cx="26" cy="26" r="24" fill="var(--paper)"/><circle cx="26" cy="26" r="20" fill="var(--ink)"/><path d="M22 14h8M23 14v8l-7 12h20l-7-12v-8" fill="none" stroke="var(--paper)" stroke-width="2.5"/></svg>Non-toxic</div>
</section>

</body>
</html>
```